Kalvora Cookbook (Independant Kalvora Consultant - not Kalvora themselves)

Approx 120 page Recipe book, need design created for recipe pages.
each recipe illustrated with full colour photograph (supplied) on opposite page.
To included index, contents page, intro, etc
Cover design also to be suggested.
We must have a professional finish, but with a friendly, family theme.
Reason: Deadline extended because I require further designs, please.

```html
<!DOCTYPE html>
<html lang="en">
<head>
<meta charset="utf-8">
<title>Kalvora Cookbook – Pecan Caramel Rolls</title>
<link rel="stylesheet" href="https://fonts.googleapis.com/css2?family=Open+Sans:wght@400;600;700&family=Cagliostro&display=swap">
<style>
  :root {
    --backdrop: #d6d6d6;
    --page: #ffffff;
    --accent: #e8628a;
    --ink: #3e3e3e;
    --rule: #9a9a9a;
    --photo-warm: #b07a4a;
    --photo-light: #ece6dc;
  }
  * { margin: 0; padding: 0; box-sizing: border-box; }
  html, body { width: 1200px; height: 1000px; overflow: hidden; }
  body { background: var(--backdrop); font-family: "Open Sans", Arial, sans-serif; position: relative; }

  .page { position: absolute; background: var(--page); box-shadow: 0 1px 4px rgba(0,0,0,.12); }
  .page--left { left: 18px; top: 157px; width: 570px; height: 711px; }
  .page--right { left: 598px; top: 159px; width: 569px; height: 709px; }

  .recipe-photo {
    position: absolute; left: 34px; top: 33px; width: 503px; height: 645px;
    background: linear-gradient(180deg, var(--photo-warm) 0%, var(--photo-light) 100%);
  }

  .ribbon { position: absolute; left: 33px; top: 0; width: 99px; height: 131px; }
  .ribbon__label {
    position: absolute; left: 33px; top: 53px; width: 99px; text-align: center;
    color: #fff; font-size: 11px;
  }
  .header-rule { position: absolute; left: 132px; top: 51px; width: 437px; height: 1px; background: var(--accent); }
  .section-label {
    position: absolute; right: 14px; top: 36px; color: var(--accent);
    font-size: 9px; letter-spacing: .5px;
  }
  .recipe-title {
    position: absolute; left: 146px; top: 98px; color: var(--accent);
    font-family: "Cagliostro", "Optima", sans-serif; font-weight: 400; font-size: 25px;
    letter-spacing: -0.4px; line-height: 1.1; white-space: nowrap;
  }

  .column-rule { position: absolute; left: 132px; top: 143px; height: 540px; border-left: 1px dotted var(--rule); }
  .block-rule { position: absolute; left: 33px; width: 502px; border-top: 1px dotted var(--rule); }

  .ingredients {
    position: absolute; left: 33px; width: 95px; color: var(--accent);
    font-size: 8.5px; line-height: 11.8px; font-weight: 600;
  }
  .ingredients h3 { font-size: 8.5px; font-weight: 700; }
  .method {
    position: absolute; left: 145px; color: var(--ink);
    font-size: 9.4px; line-height: 13px; font-weight: 600; white-space: nowrap;
  }
  .method h3 { font-size: 9.4px; font-weight: 700; line-height: 13px; }

  .folio {
    position: absolute; right: 24px; bottom: 14px; display: flex; align-items: center;
    font-size: 7px; color: #222;
  }
  .folio__name { font-weight: 700; letter-spacing: .3px; padding-right: 7px; border-right: 1px solid #bbb; height: 20px; line-height: 20px; }
  .folio__number { padding-left: 7px; font-size: 8px; }
</style>
</head>
<body>

<section class="page page--left">
  <div class="recipe-photo" role="img" aria-label="Recipe photograph: pecan caramel roll served with caramel sauce"></div>
</section>

<section class="page page--right">
  <svg class="ribbon" viewBox="0 0 99 131" aria-hidden="true">
    <polygon points="0,0 99,0 99,131 49.5,96 0,131" fill="var(--accent)"/>
  </svg>
  <span class="ribbon__label">Oven</span>
  <div class="header-rule"></div>
  <span class="section-label">DESSERT</span>
  <h1 class="recipe-title">PECAN CARAMEL ROLLS</h1>

  <div class="column-rule"></div>

  <div class="ingredients" style="top:147px">
    <h3>DOUGH</h3>
    60g butter<br>430g milk<br>155g honey<br>2½ teaspoon yeast<br>1 egg<br>820g baker's flour<br>2 teaspoons salt<br>1 cup pecans, roughly chopped
  </div>
  <div class="method" style="top:146px">
    Melt butter in bowl 2 minutes, on 90oC, Speed 2.<br>
    Add milk and honey, heat for 2 minutes, on 37oC, Speed 2.<br>
    Sprinkle yeast through hole in lid while mixing.<br>
    Let stand for 5 minutes until frothy, stir gently.<br>
    Add egg and mix in.<br>
    Add 750g flour and salt.&nbsp; Mix for 6 seconds on Speed 6.&nbsp; Knead for 2 minutes<br>
    at Interval Speed.&nbsp; Add remaining ½ cup flour if necessary.<br>
    Turn out dough onto bread mat or floured surface.&nbsp; Cut in half, shape each half into a ball.<br>
    Cover, and let rise for 1-2 hours until doubled in bulk.
  </div>

  <div class="block-rule" style="top:278px"></div>

  <div class="ingredients" style="top:290px">
    <h3>CARAMEL SAUCE</h3>
    1 ¾ cups cream<br>1 ¾ cups brown sugar
  </div>
  <div class="method" style="top:290px">
    Place cream and sugar in bowl.<br>
    Cook for 7 minutes on 90oC, Speed 2.
  </div>

  <div class="block-rule" style="top:356px"></div>

  <div class="ingredients" style="top:372px">
    <h3>CINNAMON FILLING</h3>
    1/3 cup brown sugar<br>2/3 cup castor sugar<br>1 tblspn cinnamon
  </div>
  <div class="method" style="top:374px">Mix all together in small bowl and set aside.</div>

  <div class="block-rule" style="top:445px"></div>

  <div class="method" style="top:457px">
    <h3>TO MAKE THE ROLLS</h3>
    Grease a 38 x 25 cm baking dish.<br>
    &nbsp;Spread 1½ cups caramel sauce over the base.<br>
    Roll out dough balls into 2 rectangles 38 x 23 cm with the short side facing you.<br>
    Brush with 1½ tblspns of the melted butter, sprinkle with half the cinnamon sugar.<br>
    Starting at the bottom, roll up the dough into a log.<br>
    Pinch the seam to seal.&nbsp; Cut log into 6 slices.<br>
    Arrange slices, cut side up, in prepared dish.&nbsp; Repeat with remaining dough.<br>
    Cover and let rise in warm spot until doubled in size, 45 minutes – 1 hour.<br>
    Bake in 180OC oven until rolls are golden, about 35 minutes.<br>
    Brush with remaining melted butter.&nbsp; Stand 3 minutes.<br>
    Invert onto flat tray to cool for 5 minutes.<br>
    Separate rolls with two forks.<br>
    Serve each roll on individual plate, topped with remaining warm caramel sauce<br>
    and a sprinkling of pecans.
  </div>

  <footer class="folio">
    <span class="folio__name">KALVORA COOKBOOK</span>
    <span class="folio__number">27</span>
  </footer>
</section>

</body>
</html>
```